Lakeshore Freightways Guild Web Update

Update wordpress based association web site. Please look up www.lakeshorefreightwaysguild.com for our web site to get a feel for what we currently having. We would like our updated web site to look similar to: www.brightoakline.com. We will provide our key points for updating in a future email.

Target Market(s)

duplicate the brightoakline.com format please.

Number of Pages Required

4 page

Font styles to use
Serif

Requirements
Must have
• duplicate the brightoakline.com format please. You will keep most of the content that we currently have on our website.
Nice to have
• n/a
Should not have
• n/a

```html
<!DOCTYPE html>
<html lang="en">
<head>
<meta charset="utf-8">
<title>Lakeshore Freightways Guild</title>
<link rel="stylesheet" href="https://fonts.googleapis.com/css2?family=Lato:wght@400;700;900&family=Merriweather:wght@400;700&display=swap">
<style>
:root{
  --navy:#1c1c86;
  --navy-deep:#14146a;
  --panel:rgba(28,28,134,.9);
  --heading:#2a2a8c;
  --red:#c8383d;
  --ink:#333;
  --muted:#777;
  --page:#ffffff;
  --line:#dcdce6;
}
*{box-sizing:border-box;margin:0;padding:0}
html,body{width:1200px;height:4336px;overflow:hidden;background:var(--page);font-family:"Lato",sans-serif;color:var(--ink)}
.site{position:relative;width:1200px;height:4336px}

/* header */
.site-header{position:absolute;top:0;left:0;width:1200px;height:144px;background:#fff}
.brand{position:absolute;left:112px;top:40px;display:flex;align-items:center;gap:14px}
.brand-mark{width:22px;height:22px;background:var(--navy)}
.brand-name{font-family:"Merriweather",serif;font-weight:700;color:var(--navy);font-size:22px;line-height:1.15;width:180px}
.social{position:absolute;right:112px;top:14px;display:flex;gap:18px}
.social span{width:18px;height:18px;border-radius:50%;background:var(--navy)}
.menu-btn{position:absolute;left:952px;top:72px;width:90px;height:40px;border:2px solid var(--line);font-size:15px;color:var(--muted);display:flex;align-items:center;justify-content:center;gap:10px}
.menu-btn i{display:block;width:14px;height:2px;background:var(--muted);box-shadow:0 5px 0 var(--muted),0 -5px 0 var(--muted)}
.search-btn{position:absolute;left:1048px;top:72px;width:40px;height:40px;background:var(--red);display:flex;align-items:center;justify-content:center}

/* hero */
.hero{position:absolute;top:144px;left:0;width:1200px;height:656px;background:linear-gradient(180deg,#1b2a4a 0%,#3a4c72 45%,#6e5a55 75%,#2a2522 100%)}
.hero-text{position:absolute;left:112px;top:412px;width:900px;color:#fff;font-weight:900;font-size:36px;line-height:1.3;text-shadow:0 2px 6px rgba(0,0,0,.5)}

/* section headings */
.section-title{position:absolute;left:0;width:1200px;text-align:center;font-weight:900;font-size:40px;color:var(--heading)}

/* feature bands */
.band{position:absolute;left:0;width:1200px}
.band .photo{position:absolute;inset:0}
.panel{position:absolute;background:var(--panel);color:#fff;text-align:center;padding:30px 40px;display:flex;flex-direction:column;align-items:center;justify-content:center}
.panel .icon{flex:none;width:92px;height:92px;border:3px solid rgba(255,255,255,.85);border-radius:50%;margin:0 auto 26px;display:flex;align-items:center;justify-content:center}
.panel p{font-size:15px;line-height:1.55}
.btn-outline{flex:none;display:inline-block;margin-top:28px;padding:12px 30px;border:2px solid #fff;font-size:15px;color:#fff}
.staff-photo{flex:none;width:96px;height:104px;margin:0 auto 16px;background:linear-gradient(180deg,#bcc3cc,#5a6474)}
.staff-name{font-weight:900;font-size:24px;line-height:1.2}
.staff-role{font-size:15px;margin-bottom:20px}

/* contact */
.contact{position:absolute;top:3700px;left:0;width:1200px;height:172px;background:var(--navy);color:#fff;display:flex;justify-content:center;padding:0 112px}
.contact-item{flex:1;text-align:center;padding-top:30px;font-size:16px;line-height:1.5}
.contact-item svg{display:block;margin:0 auto 18px}
.contact-item b{font-weight:700}

/* footer widgets */
.widgets{position:absolute;top:3880px;left:112px;width:976px;height:392px;display:flex;gap:40px}
.widget h4{font-weight:900;font-size:20px;color:var(--ink);margin:24px 0 14px}
.w-follow{width:320px}
.feed{width:300px;height:300px;border:1px solid var(--line);padding:12px;font-size:13px;color:var(--muted)}
.feed .feed-head{font-weight:700;color:var(--ink);border-bottom:1px solid var(--line);padding-bottom:8px;margin-bottom:10px}
.feed .feed-img{height:150px;margin-top:12px;background:linear-gradient(135deg,#e8e8ee,#c9ccd8)}
.w-vets{width:260px;text-align:center}
.w-vets h4{text-align:left}
.badge{width:170px;height:170px;margin:10px auto 16px;border-radius:50%;background:var(--navy)}
.w-vets p{font-size:15px;color:var(--ink);line-height:1.4}
.w-news{width:316px}
.news-box{background:var(--navy);padding:24px;height:300px}
.field{height:42px;background:#fff;margin-bottom:14px;padding:11px 14px;font-size:15px;color:#999}
.send{width:100%;height:44px;background:#e4e4ea;color:var(--navy);font-weight:900;font-size:17px;display:flex;align-items:center;justify-content:center;margin-bottom:18px}
.emergency{background:var(--red);color:#fff;font-weight:700;font-size:15px;text-align:center;padding:14px 10px;line-height:1.35}

.copyright{position:absolute;top:4272px;left:0;width:1200px;height:64px;border-top:1px solid var(--line);text-align:center;line-height:64px;font-size:14px;color:var(--muted)}
</style>
</head>
<body>
<div class="site">

  <header class="site-header">
    <div class="brand"><span class="brand-mark"></span><span class="brand-name">Lakeshore Freightways Guild</span></div>
    <div class="social"><span></span><span></span><span></span><span></span><span></span></div>
    <div class="menu-btn">Menu <i></i></div>
    <div class="search-btn">
      <svg width="18" height="18" viewBox="0 0 18 18"><circle cx="7.5" cy="7.5" r="5.5" fill="none" stroke="#fff" stroke-width="2"/><line x1="11.5" y1="11.5" x2="16" y2="16" stroke="#fff" stroke-width="2.4"/></svg>
    </div>
  </header>

  <section class="hero" role="img" aria-label="Freight locomotive pulling a train at dusk under a glowing sky">
    <p class="hero-text">Every year America's freight railroads spend more than $20 billion annually of their own funds, not taxpayer money, to build and maintain a rail network that is safe, reliable, efficient and affordable.</p>
  </section>

  <h2 class="section-title" style="top:830px">What We Do</h2>
  <section class="band" style="top:920px;height:528px">
    <div class="photo" role="img" aria-label="Blue and white locomotive parked in a rail yard" style="background:linear-gradient(120deg,#9fb8d8 0%,#3c5fa6 40%,#1f2f6a 70%,#6b7a8a 100%)"></div>
    <div class="panel" style="left:620px;top:40px;width:480px;height:448px">
      <div class="icon"><svg width="44" height="44" viewBox="0 0 48 48" fill="none" stroke="#fff" stroke-width="3"><line x1="24" y1="4" x2="24" y2="44"/><path d="M24 10h14l5 5-5 5H24"/><path d="M24 24H10l-5 5 5 5h14"/></svg></div>
      <p>The LFG reviews all introduced legislation in the House and Senate. Proposed legislation affecting the rail industry is shared with our members. Final industry positions regarding legislation are then communicated to the legislature. We pursue the same actively with appropriate personnel in the state departments and the legislative rules process.</p>
      <span class="btn-outline">Learn More</span>
    </div>
  </section>

  <h2 class="section-title" style="top:1492px">Who We Are</h2>
  <section class="band" style="top:1568px;height:544px">
    <div class="photo" role="img" aria-label="Orange and black freight locomotive passing green trees by the water" style="background:linear-gradient(110deg,#8fb0c8 0%,#5d8a52 45%,#2f5a2a 65%,#c98a2a 85%,#3a3a3a 100%)"></div>
    <div class="panel" style="left:112px;top:40px;width:480px;height:464px">
      <div class="icon"><svg width="40" height="44" viewBox="0 0 44 48" fill="none" stroke="#fff" stroke-width="3"><path d="M22 4a14 14 0 0 0-8 25v6h16v-6a14 14 0 0 0-8-25z"/><line x1="15" y1="41" x2="29" y2="41"/></svg></div>
      <p>The Lakeshore Freightways Guild (LFG) is a non-profit trade association that represents the interests of freight railroads operating in the Great Lakes region. LFG members range in size from large Class I interstate carriers to smaller regional carriers and shortline railroads. LFG members account for over 95% of all freight rail moved in the region.</p>
      <span class="btn-outline">Learn More</span>
    </div>
  </section>

  <h2 class="section-title" style="top:2128px">LFG Staff</h2>
  <section class="band" style="top:2200px;height:580px">
    <div class="photo" role="img" aria-label="Red locomotive plowing through snow" style="background:linear-gradient(120deg,#2d4f86 0%,#5c82b8 30%,#9b2a2a 50%,#d8dde6 80%,#f2f4f8 100%)"></div>
    <div class="panel" style="left:620px;top:40px;width:468px;height:500px;padding:26px 36px">
      <div class="staff-photo" role="img" aria-label="Portrait of the guild president"></div>
      <div class="staff-name">Dale Whitmore</div>
      <div class="staff-role">President</div>
      <p style="font-size:14px;line-height:1.5">I would like to welcome you to the Lakeshore Freightways Guild website. Here you will find valuable information on regional railroads, including issues and concerns in and around the railroad industry. We are an active and aggressive state railroad association and we look forward to continued success with our partnerships. Please make sure to click on our member railroad company links while you're here. Also, sign up for our newsletter and follow the LFG on Chirper. Thank you and I hope you enjoy your visit to our website.</p>
    </div>
  </section>

  <h2 class="section-title" style="top:2844px">How to Join LFG</h2>
  <section class="band" style="top:2932px;height:648px">
    <div class="photo" role="img" aria-label="Orange and navy locomotive numbered 2019 among autumn trees" style="background:linear-gradient(110deg,#6d7a4a 0%,#3e5a2e 40%,#d9892a 60%,#1f2a5a 80%,#b7c2cc 100%)"></div>
    <div class="panel" style="left:112px;top:40px;width:480px;height:568px">
      <div class="icon"><svg width="42" height="42" viewBox="0 0 46 46" fill="none" stroke="#fff" stroke-width="3"><circle cx="23" cy="15" r="9"/><path d="M6 42c2-10 9-15 17-15s15 5 17 15"/></svg></div>
      <p>LFG membership is open to any freight railroad with operations in the region. Please contact the LFG office for membership information.</p>
      <p style="margin-top:18px">Companies which supply goods or services to the railroad industry are eligible for a non-voting Associate Membership. Annual dues are $1,000 per year for supplier members.</p>
      <p style="margin-top:18px">Please click HERE to download the LFG Associate Membership application. Return a completed form to info@lakeshorefreightwaysguild.com or mail to our mailing address.</p>
      <span class="btn-outline">Meet Our Member</span>
    </div>
  </section>

  <h2 class="section-title" style="top:3616px">Get In Touch</h2>
  <section class="contact">
    <div class="contact-item">
      <svg width="26" height="34" viewBox="0 0 26 34" fill="none" stroke="#fff" stroke-width="2.4"><path d="M13 32s11-12 11-19a11 11 0 0 0-22 0c0 7 11 19 11 19z"/><circle cx="13" cy="13" r="4"/></svg>
      450 Harbor Street,<br>Suite 210 Portage, MI 49002
    </div>
    <div class="contact-item">
      <svg width="30" height="30" viewBox="0 0 30 30" fill="none" stroke="#fff" stroke-width="2.4"><path d="M7 3l5 6-3 3c2 4 5 7 9 9l3-3 6 5-3 4C13 27 3 17 3 6z"/></svg>
      <b>Call us :</b><br>(555) 214-0187
    </div>
    <div class="contact-item">
      <svg width="30" height="30" viewBox="0 0 30 30" fill="none" stroke="#fff" stroke-width="2.4"><rect x="4" y="11" width="22" height="12"/><rect x="8" y="4" width="14" height="7"/><rect x="8" y="19" width="14" height="8"/></svg>
      <b>Fax :</b><br>(555) 214-0188
    </div>
    <div class="contact-item" style="flex:1.4">
      <svg width="32" height="24" viewBox="0 0 32 24" fill="none" stroke="#fff" stroke-width="2.4"><rect x="2" y="2" width="28" height="20"/><path d="M2 3l14 11L30 3"/></svg>
      <b>Email Us :</b><br>info@lakeshorefreightwaysguild.com
    </div>
  </section>

  <section class="widgets">
    <div class="widget w-follow">
      <h4>Follow LFG</h4>
      <div class="feed">
        <div class="feed-head">Tweets by @LakeshoreFG</div>
        <div>Lakeshore Freightways Guild @LakeshoreFG</div>
        <div>Join us in promoting rail safety this week</div>
        <div class="feed-img" role="img" aria-label="Rail safety week promotional graphic"></div>
      </div>
    </div>
    <div class="widget w-vets">
      <h4>Railroads &amp; Veterans</h4>
      <div class="badge"></div>
      <p>Click HERE to learn which<br>railroads hire veterans.</p>
    </div>
    <div class="widget w-news">
      <h4>Join Our Newsletter List</h4>
      <div class="news-box">
        <div class="field">Your Name (required)</div>
        <div class="field">Your Email (required)</div>
        <div class="send">SEND</div>
        <div class="emergency">Railroad Company Emergency<br>Phone Numbers</div>
      </div>
    </div>
  </section>

  <footer class="copyright">Copyright © 2017 Lakeshore Freightways Guild. All rights reserved.</footer>
</div>
</body>
</html>
```